New women's health clinic needs a new home!!

We need a professional website for our modern women's health clinic. Needs to be in wordpress. Back end needs to be accesible by novice admin staff. Text and stock photography supplied by us. We need approximately 5 pages with 3-4 subpages each. Links to social media a must. Blog a must. Patients will need to be able to download e-books after supplying an e-mail address. Mobile-friendly is a must!

We created our logo through this site. Please refer to the logo for style themes.

Target Market(s)

Women aged 28-55

Industry/Entity Type

Health

Coding

Coded - Design and coding required

Number of Pages Required

5+ page

Font styles to use
Sans Serif

Colors
886aae
cee9f5
3377b5
d3a5cc
ffffff
eddcec
6e479c
85abd2
876aae

Requirements
Must have
• Wordpress
• Social media ready
• Mobile-friendly to Plinexa's specs
• Ability to download e-books
• Captures data on back end

```html
<!DOCTYPE html>
<html lang="en">
<head>
<meta charset="utf-8">
<title>Aurelle Women's Health – Women's Health Clinic</title>
<link href="https://fonts.googleapis.com/css2?family=Arimo:ital,wght@0,400;0,700;1,400&family=Mulish:wght@400;600&display=swap" rel="stylesheet">
<style>
:root{
  --purple:#6e479c;
  --purple-mid:#886aae;
  --purple-dark:#5a3a86;
  --blue:#3377b5;
  --blue-soft:#85abd2;
  --sky:#8fc9e6;
  --pink:#d3a5cc;
  --pink-strong:#c983c7;
  --lilac:#eddcec;
  --text:#555;
  --muted:#888;
  --white:#fff;
  --footer-bg:#f5f5f5;
  --footer-bar:#7a57a5;
}
*{margin:0;padding:0;box-sizing:border-box}
html,body{width:697px;height:1200px;overflow:hidden;background:var(--white)}
body{position:relative;font-family:"Arimo",Arial,sans-serif;color:var(--text)}
h2,h3,h4{font-weight:400}
.abs{position:absolute}

/* header */
.brand{left:0;width:697px;top:10px;text-align:center}
.brand-dot{display:block;margin:0 auto 6px;width:44px;height:44px;border-radius:50%;background:var(--purple-mid)}
.brand-name{font-family:"Arimo",Arial,sans-serif;font-weight:700;font-size:9.5px;letter-spacing:.6px;line-height:10px;color:#222}

.nav{left:58px;top:91px;width:582px;height:33px;display:flex;z-index:5;background:linear-gradient(#8a6bb3,#7556a1)}
.nav a{display:flex;align-items:center;justify-content:center;height:33px;color:var(--white);text-decoration:none;font-family:"Mulish",sans-serif;font-size:8px;line-height:1;text-transform:uppercase;border-right:1px solid rgba(255,255,255,.15)}
.nav a.active{background:linear-gradient(#6b4c98,#573b86)}

/* hero */
.hero{left:0;top:111px;width:697px;height:272px;z-index:1;background:linear-gradient(100deg,#c9a7b6 0%,#b89aa8 30%,#d8c1b8 55%,#e2cfc4 70%,#8d9a6c 100%)}
.hero-title{left:58px;top:193px;z-index:2;font-family:"Arimo",Arial,sans-serif;font-weight:700;font-size:30px;line-height:34px}
.hero-title .l1{color:var(--purple-mid)}
.hero-title .l2{color:var(--blue)}
.hero-text{left:58px;top:270px;z-index:2;width:290px;font-size:7.2px;line-height:13px;color:var(--white);text-transform:uppercase}
.hero-next{left:647px;top:232px;z-index:2}

/* welcome */
.welcome-title{left:0;width:697px;top:411px;text-align:center;font-size:14px;color:#555;letter-spacing:.2px}
.welcome-sub{left:0;width:697px;top:435px;text-align:center;font-size:9px;font-style:italic;color:var(--pink-strong)}
.card{top:469px;width:136px;height:191px;border:1px solid #e3e3e3;text-align:center}
.card-photo{height:99px}
.card h3{margin-top:13px;font-family:"Mulish",sans-serif;font-size:7.5px;color:var(--purple);text-transform:uppercase}
.card p{margin:6px 6px 0;font-size:5.8px;line-height:11px;color:#666}
.card .btn{display:inline-block;margin-top:8px;width:53px;height:18px;line-height:16px;border:1px solid var(--purple);border-radius:9px;font-family:"Mulish",sans-serif;font-size:6.5px;color:var(--purple);text-decoration:none}

/* ebook band */
.ebook{left:0;top:685px;width:697px;height:105px;background:var(--sky)}
.ebook-art{left:60px;top:694px;width:120px;height:79px;border-radius:4px;background:linear-gradient(#5fb7e6,#3a3a3a)}
.ebook-title{left:192px;top:707px;font-weight:700;font-size:17px;color:var(--white)}
.ebook-text{left:194px;top:735px;width:300px;font-size:6px;line-height:12px;font-style:italic;color:var(--white)}
.ebook-btn{left:517px;top:729px;width:117px;height:23px;border:1px solid var(--white);border-radius:12px;text-align:center;line-height:21px;font-style:italic;font-size:9.5px;color:var(--white)}

/* lower section */
.col-title{top:815px;font-size:13px;color:#444;letter-spacing:.3px;text-transform:uppercase}
.about-sub{left:58px;top:844px;font-size:8px;color:#555}
.about-text{left:58px;width:185px;font-size:5.8px;line-height:11px;font-style:italic;color:var(--muted)}
.about-more{left:58px;top:1006px;font-family:"Mulish",sans-serif;font-style:italic;font-weight:600;font-size:7.5px;color:var(--purple)}

.news{left:266px;width:180px}
.news-date{position:absolute;left:0;top:0;width:36px;height:36px;border-radius:50%;color:var(--white);text-align:center;font-family:Georgia,serif;font-style:italic;font-size:8px;line-height:9px;padding-top:9px}
.news-body{position:absolute;left:47px;top:0;width:130px}
.news-body h4{font-size:8px;color:#555}
.news-body p{margin-top:5px;font-size:5.5px;line-height:11px;font-style:italic;color:var(--muted)}
.news-body span{display:block;margin-top:3px;font-size:6px;font-style:italic;color:var(--blue-soft)}

.gallery{left:463px;top:845px;display:grid;grid-template-columns:repeat(3,57px);grid-auto-rows:57px;gap:2px}

/* footer */
.footer{left:0;top:1054px;width:697px;height:111px;background:var(--footer-bg)}
.foot-title{top:1071px;font-size:9.5px;color:#444;text-transform:uppercase}
.foot-text{font-size:5.8px;line-height:11px;font-style:italic;color:var(--muted)}
.social{left:58px;top:1131px;display:flex;gap:3px}
.social span{width:17px;height:17px;border-radius:50%}
.loc{left:270px;display:flex;align-items:center;gap:8px;font-size:5.8px;font-style:italic;color:var(--muted);line-height:10px}
.news-form{left:467px;top:1119px;width:173px;height:22px;display:flex}
.news-form .field{flex:1;border:1px solid #ccc;border-right:none;border-radius:11px 0 0 11px;background:var(--white);font-size:6px;color:#555;line-height:20px;padding-left:9px}
.news-form .send{width:53px;background:var(--pink-strong);color:var(--white);border-radius:0 11px 11px 0;font-size:6.5px;text-align:center;line-height:22px}
.bottom-bar{left:0;top:1165px;width:697px;height:35px;background:var(--footer-bar);text-align:center;color:var(--white);font-size:6px;line-height:35px}
</style>
</head>
<body>

<header>
  <div class="abs brand">
    <span class="brand-dot"></span>
    <div class="brand-name">AURELLE<br>WOMEN'S HEALTH</div>
  </div>
  <nav class="abs nav">
    <a class="active" style="width:76px">Home</a>
    <a style="width:90px">About Us</a>
    <a style="width:86px">Services</a>
    <a style="width:72px">Blog</a>
    <a style="width:82px">Gallery</a>
    <a style="width:77px">News</a>
    <a style="width:99px;border-right:none">Contact Us</a>
  </nav>
</header>

<section>
  <div class="abs hero" role="img" aria-label="Smiling woman outdoors with a towel over her shoulder, soft blurred park behind"></div>
  <h1 class="abs hero-title"><span class="l1">WOMEN'S</span><br><span class="l2">HEALTH CLINIC</span></h1>
  <p class="abs hero-text">It is a long established fact that a reader will be distracted by the readable content of a page when looking at its layout. The point of look like readable English.....</p>
  <svg class="abs hero-next" width="34" height="34" viewBox="0 0 34 34" aria-label="Next slide">
    <circle cx="17" cy="17" r="15.5" fill="rgba(255,255,255,.15)" stroke="rgba(255,255,255,.7)" stroke-width="1.5"/>
    <path d="M13 9 L23 17 L13 25 Z" fill="none" stroke="rgba(255,255,255,.8)" stroke-width="1.5"/>
  </svg>
</section>

<section>
  <h2 class="abs welcome-title">WELCOME TO WOMEN’S HEALTH CLINIC</h2>
  <p class="abs welcome-sub">It is a long established fact that a reader will be distracted by the readable looking at its layout.</p>

  <article class="abs card" style="left:58px">
    <div class="card-photo" role="img" aria-label="Women stretching in a yoga class" style="background:linear-gradient(#d9dde3,#a9b4c4)"></div>
    <h3>Contrary to popular</h3>
    <p>It is a long established fact that a reader will be distracted by the readable content of a page when looking at its layout.</p>
    <a class="btn">Read More</a>
  </article>
  <article class="abs card" style="left:206px">
    <div class="card-photo" role="img" aria-label="Group fitness class in a gym" style="background:linear-gradient(#e8e2d8,#c9a27a)"></div>
    <h3>Contrary to popular</h3>
    <p>It is a long established fact that a reader will be distracted by the readable content of a page when looking at its layout.</p>
    <a class="btn">Read More</a>
  </article>
  <article class="abs card" style="left:354px">
    <div class="card-photo" role="img" aria-label="Woman meditating by the sea" style="background:linear-gradient(#8fc2ea,#2f6fa8)"></div>
    <h3>Contrary to popular</h3>
    <p>It is a long established fact that a reader will be distracted by the readable content of a page when looking at its layout.</p>
    <a class="btn">Read More</a>
  </article>
  <article class="abs card" style="left:502px">
    <div class="card-photo" role="img" aria-label="People riding exercise bikes in a spin class" style="background:linear-gradient(#f2f2f2,#d86aa0 60%,#3a3a3a)"></div>
    <h3>Contrary to popular</h3>
    <p>It is a long established fact that a reader will be distracted by the readable content of a page when looking at its layout.</p>
    <a class="btn">Read More</a>
  </article>
</section>

<section>
  <div class="abs ebook"></div>
  <div class="abs ebook-art" role="img" aria-label="Tablet showing a download e-book speech bubble"></div>
  <h2 class="abs ebook-title">WOMEN'S HEALTH CLINIC</h2>
  <p class="abs ebook-text">It is a long established fact that a reader will be distracted by the readable content of a page when looking at its layout. The point of using Lorem normal distribution of letters, as opposed to using 'Content here, content here', making it look like readable English....</p>
  <div class="abs ebook-btn">e-book download</div>
</section>

<section>
  <h2 class="abs col-title" style="left:58px">About Us</h2>
  <h3 class="abs about-sub">Neque porro quisquam est</h3>
  <p class="abs about-text" style="top:865px">It is a long established fact that a reader will be distracted by the readable content of a page when looking at its layout. The point of using Lorem Ipsum is that it has a more-or-less normal distribution of letters, as opposed to using 'Content here, content here', making it look like readable English. Many desktop publishing packages and web page editors now use Lorem Ipsum as their default model text, will uncover many web sites still in their infancy..</p>
  <p class="abs about-text" style="top:950px">'Content here, content here', making it look like readable English. Many desktop publishing packages and web page editors now use Lorem Ipsum as their default model text, will uncover many web sites still in their infancy.......</p>
  <a class="abs about-more">Read More</a>

  <h2 class="abs col-title" style="left:269px">Latest News</h2>
  <div class="abs news" style="top:845px">
    <div class="news-date" style="background:#e5a6d8">14<br>Mar</div>
    <div class="news-body"><h4>Neque porro quisquam est</h4><p>It is a long established fact that a reader will be when looking at its layout.....</p><span style="color:var(--pink)">Read More</span></div>
  </div>
  <div class="abs news" style="top:906px">
    <div class="news-date" style="background:var(--blue-soft)">14<br>Mar</div>
    <div class="news-body"><h4>Neque porro quisquam est</h4><p>It is a long established fact that a reader will be when looking at its layout.....</p><span>Read More</span></div>
  </div>
  <div class="abs news" style="top:971px">
    <div class="news-date" style="background:#a8cde0">14<br>Mar</div>
    <div class="news-body"><h4>Neque porro quisquam est</h4><p>It is a long established fact that a reader will be when looking at its layout.....</p><span style="color:#a8cde0">Read More</span></div>
  </div>

  <h2 class="abs col-title" style="left:462px">Our Gallery</h2>
  <div class="abs gallery">
    <div role="img" aria-label="Woman jumping under a blue sky" style="background:linear-gradient(#bfe0f5,#9cc36a)"></div>
    <div role="img" aria-label="Woman relaxing outdoors" style="background:linear-gradient(#4a3a2a,#c9a27a)"></div>
    <div role="img" aria-label="Spin class" style="background:linear-gradient(#f0f0f0,#d86aa0)"></div>
    <div role="img" aria-label="Exercise ball workout" style="background:linear-gradient(#e8d84a,#4a8ad0)"></div>
    <div role="img" aria-label="Woman holding an apple" style="background:linear-gradient(#e8c09a,#d0402f)"></div>
    <div role="img" aria-label="Woman running in a field" style="background:linear-gradient(#bfdcf0,#7cb04a)"></div>
    <div role="img" aria-label="Yoga pose on a pier" style="background:linear-gradient(#d6e4ea,#8aa2a8)"></div>
    <div role="img" aria-label="Woman meditating" style="background:linear-gradient(#f5f5f5,#d0c4b8)"></div>
    <div role="img" aria-label="Stretching on a yoga mat" style="background:linear-gradient(#e8d0d8,#3a5a9a)"></div>
  </div>
</section>

<footer>
  <div class="abs footer"></div>
  <h2 class="abs foot-title" style="left:58px">Stay in Touch!</h2>
  <p class="abs foot-text" style="left:58px;top:1089px;width:185px">Follow US in our social networks! Lorem ipsum dolor sit amet, conse It is a long established fact that a reader will be distracted by the a page cletur and go adipiscing elit.</p>
  <div class="abs social" aria-label="Social links">
    <span style="background:#3b5998"></span>
    <span style="background:#1da1f2"></span>
    <span style="background:#d34836"></span>
    <span style="background:#e0245e"></span>
    <span style="background:#f2b21f"></span>
  </div>

  <h2 class="abs foot-title" style="left:271px">Our Location</h2>
  <div class="abs loc" style="top:1089px">
    <svg width="7" height="9" viewBox="0 0 7 9"><path d="M3.5 0A3.5 3.5 0 0 0 0 3.5C0 6 3.5 9 3.5 9S7 6 7 3.5A3.5 3.5 0 0 0 3.5 0Zm0 5A1.5 1.5 0 1 1 3.5 2a1.5 1.5 0 0 1 0 3Z" fill="#999"/></svg>
    <span>Address : 5224 Women Health Lorem Ipsum<br>Dummy Text</span>
  </div>
  <div class="abs loc" style="top:1116px">
    <svg width="8" height="8" viewBox="0 0 8 8"><path d="M1.6 0.3 3 1.8 2.2 3C2.7 4 4 5.3 5 5.8L6.2 5 7.7 6.4 6.8 7.7C3.5 7.5 .5 4.5.3 1.2Z" fill="#999"/></svg>
    <span>Phone : (321) 555-0147</span>
  </div>
  <div class="abs loc" style="top:1134px">
    <svg width="8" height="6" viewBox="0 0 8 6"><rect width="8" height="6" fill="#999"/><path d="M0 0 4 3.2 8 0" fill="none" stroke="#f5f5f5" stroke-width=".8"/></svg>
    <span>Email : office@aurellehealth.org</span>
  </div>

  <h2 class="abs foot-title" style="left:467px">Newsletter</h2>
  <p class="abs foot-text" style="left:467px;top:1089px;width:180px">Lorem ipsum dolor sit amet, consectetur adi sollicitud ante tellus ornare mi, et mollis</p>
  <div class="abs news-form"><div class="field">Enter Your Email Id :</div><div class="send">SUBSCRIBE</div></div>

  <div class="abs bottom-bar">© Copy Right 2105 Women's Health Clinic.All copyrights Reserved.</div>
</footer>

</body>
</html>
```